Printed Promo Flyer for new pet business

We need a double sided flyer design as per the given example flyer, just better looking and more fun.Flyers will need to be printed.Flyer size approx 10.5cm x 15cm. The text will need to be amended slightly afterwards to be more fun unless you can create a new tone of voice as well (should sound fun like breezy do it) Look and Feel: emotional, fun, loving, professional
See attached files.

Target Market(s)

Pet owners in the UK who want the convenience of getting their pets parasite treatment delivered to their door without the need of having to run to the vet or store for purchase

Industry/Entity Type

Pet Care

Colors
00a990
6b449b

Requirements
Must have
• all the content context as given in the example flyer.
Nice to have
• Tone of voice can be changed to be more fun (using Breezy as a guide)

```html
<!DOCTYPE html>
<html lang="en">
<head>
<meta charset="utf-8">
<title>Paw Parcel – Protection and Care for Your Pet</title>
<link rel="stylesheet" href="https://fonts.googleapis.com/css2?family=Montserrat:wght@800&family=Oswald:wght@400;600&display=swap">
<style>
  :root {
    --purple: #6b449b;
    --purple-deep: #65318e;
    --teal: #1e9e96;
    --white: #ffffff;
    --fur-light: #e9c18f;
    --fur-mid: #c98b4c;
    --tabby: #9d9486;
  }
  * { margin: 0; padding: 0; box-sizing: border-box; }
  html, body {
    width: 840px;
    height: 1200px;
    overflow: hidden;
    background: var(--white);
  }
  .flyer {
    position: relative;
    width: 840px;
    height: 1200px;
    overflow: hidden;
    background: var(--white);
  }
  .flyer__shapes {
    position: absolute;
    inset: 0;
  }
  .headline {
    position: absolute;
    top: 38px;
    left: 0;
    width: 840px;
    text-align: center;
    font-family: "Montserrat", sans-serif;
    font-weight: 800;
    font-size: 66px;
    line-height: 88px;
    color: var(--white);
    letter-spacing: -0.5px;
  }
  .pet-line {
    position: absolute;
    top: 276px;
    left: 62px;
    font-family: "Oswald", sans-serif;
    font-weight: 400;
    font-size: 160px;
    line-height: 160px;
    color: var(--purple);
    letter-spacing: 0;
    white-space: nowrap;
    transform: scaleX(0.79);
    transform-origin: left top;
  }
  .pet-photo {
    position: absolute;
    left: 42px;
    top: 462px;
    width: 720px;
    height: 336px;
    border-radius: 6px;
    background: linear-gradient(100deg, var(--fur-light) 0%, var(--fur-mid) 38%, #f4ece3 55%, var(--tabby) 75%, #e8e3dc 100%);
    opacity: 0.85;
  }
  .with-label {
    position: absolute;
    left: 62px;
    top: 800px;
    font-family: "Montserrat", sans-serif;
    font-weight: 800;
    font-size: 46px;
    line-height: 1;
    color: var(--teal);
  }
  .brand-badge {
    position: absolute;
    left: 96px;
    top: 873px;
    width: 302px;
    height: 302px;
    border-radius: 50%;
    border: 7px solid var(--purple);
    background: var(--white);
    display: flex;
    align-items: center;
    justify-content: center;
  }
  .brand-badge__name {
    font-family: "Oswald", sans-serif;
    font-weight: 400;
    font-size: 44px;
    line-height: 1;
    color: var(--purple);
    letter-spacing: 1px;
    white-space: nowrap;
  }
  .love-line {
    position: absolute;
    left: 441px;
    top: 905px;
    width: 399px;
    text-align: center;
    font-family: "Oswald", sans-serif;
    font-weight: 600;
    font-size: 64px;
    line-height: 80px;
    color: var(--white);
  }
  .love-line__accent { color: var(--purple); }
</style>
</head>
<body>
<main class="flyer">
  <svg class="flyer__shapes" width="840" height="1200" viewBox="0 0 840 1200" aria-hidden="true">
    <polygon class="teal-band" points="441,275 840,190 840,1200 441,1200" fill="var(--teal)"/>
    <polygon class="top-banner" points="0,0 840,0 840,190 466,275 0,198" fill="var(--purple-deep)"/>
    <rect class="photo-panel" x="0" y="445" width="783" height="403" fill="var(--white)"/>
  </svg>

  <h1 class="headline">The Best Protection<br>and Care</h1>
  <p class="pet-line">FOR YOUR PET</p>

  <div class="pet-photo" role="img" aria-label="Photo of a smiling golden dog and a tabby cat resting their paws on a white ledge"></div>

  <p class="with-label">with</p>
  <div class="brand-badge">
    <span class="brand-badge__name">PAW PARCEL</span>
  </div>

  <p class="love-line">Your PETS<br>will <span class="love-line__accent">LOVE</span><br>you for it!</p>
</main>
</body>
</html>
```